Alterations to existing business card

Here is my current logo and I want the "cafe and bar" taken off with just the words Zolta and our slogan "Savour every sip" on the card, Plus the logo.
Our Current Business Card is currently 5.5cm by 5.5cm and would like it to remain like this thanks.
The loyalty card can be 10 squares with the logo specifying the 10th coffee free. I would like the cheapest option please.
Also on our business card would like the Facebook logo and instagram Logo with BRUNOZOLTA27 as link to our photos on instagram.

Keep Colour schemes the same please.

On the business cards

Dale Whitford Director
0427691038
dale47zolta@mailvista.example

Paula Derosio Principal
0428905713
paulzolta@mailvista.example

Thanks Dale

Industry/Entity Type

Business

```html
<!DOCTYPE html>
<html lang="en">
<head>
<meta charset="utf-8">
<title>Zolta — Business Card and Loyalty Card</title>
<link rel="stylesheet" href="https://fonts.googleapis.com/css2?family=Questrial&family=Montserrat:wght@700&display=swap">
<style>
  :root {
    --backdrop: #3b3b3b;
    --card: #ffffff;
    --ink: #111111;
    --black: #000000;
    --gold: #e8a532;
    --gold-light: #f6c65a;
    --gold-deep: #b87416;
    --white: #ffffff;
    --stamp-line: #333333;
  }
  * { box-sizing: border-box; margin: 0; padding: 0; }
  html, body { width: 1105px; height: 1200px; overflow: hidden; }
  body {
    background: var(--backdrop);
    position: relative;
    font-family: "Questrial", "Century Gothic", sans-serif;
  }
  .card {
    position: absolute;
    width: 449px;
    height: 449px;
    background: var(--card);
    overflow: hidden;
  }
  .business-card { left: 124px; top: 110px; }
  .loyalty-card { left: 500px; top: 630px; }

  .card-arc { position: absolute; inset: 0; width: 449px; height: 449px; }

  .brand-name {
    position: absolute;
    color: var(--ink);
    line-height: 1;
    letter-spacing: 2px;
  }
  .brand-slogan {
    position: absolute;
    color: var(--gold);
    letter-spacing: 1.5px;
    line-height: 1;
    text-transform: uppercase;
    white-space: nowrap;
  }
  .business-card .brand-name { left: 44px; top: 46px; font-size: 58px; }
  .business-card .brand-slogan { left: 46px; top: 102px; font-size: 13px; }

  .contact {
    position: absolute;
    right: 42px;
    text-align: right;
    color: var(--white);
    line-height: 1;
    white-space: nowrap;
  }
  .contact-name { top: 254px; font-size: 27px; color: var(--gold); letter-spacing: 0.5px; }
  .contact-role { top: 287px; font-size: 18px; letter-spacing: 0.5px; }
  .contact-line {
    display: flex;
    align-items: center;
    justify-content: flex-end;
    gap: 10px;
    font-size: 18px;
  }
  .contact-phone { top: 327px; }
  .contact-email { top: 356px; font-size: 17px; }
  .contact-social {
    top: 394px;
    font-family: "Montserrat", sans-serif;
    font-weight: 700;
    font-size: 16px;
    letter-spacing: 0.5px;
    gap: 6px;
  }
  .contact-icon { width: 18px; height: 18px; flex: none; }
  .social-dot {
    width: 20px; height: 20px; border-radius: 50%;
    background: var(--gold); flex: none;
  }
  .social-dot:first-of-type { margin-left: 4px; }

  .loyalty-card .brand-ring {
    position: absolute;
    left: 162px; top: 50px;
    width: 126px; height: 126px;
    border-radius: 50%;
    border: 4px solid var(--gold);
  }
  .loyalty-card .brand-name {
    left: 0; right: 0; top: 190px;
    text-align: center; font-size: 50px;
  }
  .loyalty-card .brand-slogan {
    left: 0; right: 0; top: 238px;
    text-align: center; font-size: 11px;
  }

  .stamp-grid {
    position: absolute;
    left: 38px; top: 275px;
    display: grid;
    grid-template-columns: repeat(5, 64px);
    column-gap: 10px;
    row-gap: 14px;
  }
  .stamp { width: 64px; height: 64px; display: block; color: var(--ink); }
  .stamp-free { color: var(--gold-deep); }
</style>
</head>
<body>
  <svg width="0" height="0" style="position:absolute" aria-hidden="true">
    <defs>
      <g id="cup">
        <path d="M26 22 q-3 -4 0 -7 q3 -3 0 -6" fill="none" stroke="currentColor" stroke-width="1.6" stroke-linecap="round"/>
        <path d="M32 22 q-3 -4 0 -7 q3 -3 0 -6" fill="none" stroke="currentColor" stroke-width="1.6" stroke-linecap="round"/>
        <path d="M19 27 h24 v5 a9 9 0 0 1 -9 9 h-6 a9 9 0 0 1 -9 -9 z" fill="currentColor"/>
        <path d="M42 29 a5 5 0 0 1 0 10 h-2" fill="none" stroke="currentColor" stroke-width="2.6"/>
        <rect x="15" y="42" width="32" height="3" rx="1.5" fill="currentColor"/>
      </g>
      <g id="stamp-ring">
        <circle cx="32" cy="32" r="30" fill="none" stroke="var(--stamp-line)" stroke-width="2"/>
        <circle cx="32" cy="32" r="26" fill="none" stroke="var(--stamp-line)" stroke-width="1"/>
      </g>
    </defs>
  </svg>

  <section class="card business-card" aria-label="Business card">
    <svg class="card-arc" viewBox="0 0 325 325" aria-hidden="true">
      <circle cx="262" cy="332" r="240" fill="var(--black)"/>
      <circle cx="262" cy="332" r="232" fill="none" stroke="var(--gold)" stroke-width="8"/>
      <circle cx="262" cy="332" r="221" fill="none" stroke="var(--gold-light)" stroke-width="2.5"/>
    </svg>

    <p class="brand-name">ZOLTA</p>
    <p class="brand-slogan">Savour every sip</p>

    <p class="contact contact-name">DALE WHITFORD</p>
    <p class="contact contact-role">DIRECTOR</p>
    <p class="contact contact-line contact-phone">
      <span>0427691038</span>
      <svg class="contact-icon" viewBox="0 0 18 18" aria-hidden="true">
        <rect x="4" y="1" width="10" height="16" rx="2" fill="none" stroke="var(--gold)" stroke-width="2"/>
        <rect x="7" y="13.5" width="4" height="1.5" fill="var(--gold)"/>
      </svg>
    </p>
    <p class="contact contact-line contact-email">
      <span>dale47zolta@mailvista.example</span>
      <svg class="contact-icon" viewBox="0 0 18 18" aria-hidden="true">
        <rect x="1" y="4" width="16" height="11" fill="var(--gold)"/>
        <path d="M1 4 l8 6 l8 -6" fill="none" stroke="var(--black)" stroke-width="1.3"/>
      </svg>
    </p>
    <p class="contact contact-line contact-social">
      <span>BRUNOZOLTA27</span>
      <span class="social-dot" aria-hidden="true"></span>
      <span class="social-dot" aria-hidden="true"></span>
    </p>
  </section>

  <section class="card loyalty-card" aria-label="Loyalty card">
    <span class="brand-ring" aria-hidden="true"></span>
    <p class="brand-name">ZOLTA</p>
    <p class="brand-slogan">Savour every sip</p>

    <div class="stamp-grid">
      <svg class="stamp" viewBox="0 0 64 64"><use href="#stamp-ring"/><use href="#cup"/></svg>
      <svg class="stamp" viewBox="0 0 64 64"><use href="#stamp-ring"/><use href="#cup"/></svg>
      <svg class="stamp" viewBox="0 0 64 64"><use href="#stamp-ring"/><use href="#cup"/></svg>
      <svg class="stamp" viewBox="0 0 64 64"><use href="#stamp-ring"/><use href="#cup"/></svg>
      <svg class="stamp" viewBox="0 0 64 64"><use href="#stamp-ring"/><use href="#cup"/></svg>
      <svg class="stamp" viewBox="0 0 64 64"><use href="#stamp-ring"/><use href="#cup"/></svg>
      <svg class="stamp" viewBox="0 0 64 64"><use href="#stamp-ring"/><use href="#cup"/></svg>
      <svg class="stamp" viewBox="0 0 64 64"><use href="#stamp-ring"/><use href="#cup"/></svg>
      <svg class="stamp" viewBox="0 0 64 64"><use href="#stamp-ring"/><use href="#cup"/></svg>
      <svg class="stamp stamp-free" viewBox="0 0 64 64">
        <circle cx="32" cy="32" r="31" fill="var(--gold)"/>
        <circle cx="32" cy="32" r="27" fill="none" stroke="var(--gold-deep)" stroke-width="1"/>
        <g transform="translate(8 0) scale(0.75)"><use href="#cup"/></g>
        <text x="32" y="47" text-anchor="middle" font-family="Montserrat, sans-serif" font-weight="700" font-size="13" fill="var(--ink)">FREE</text>
      </svg>
    </div>
  </section>
</body>
</html>
```